Landing Page Only for text marketing service msgzeta.net

Our current site msgzeta.net needs a custom landing page for paid advertisements that is conversion centered as well as clear and concise. We want to focus on displaying the information effectively without getting too wordy or confusing to gain a higher conversion rate as our main goal.

We want more emphasis on the Try for $1 that includes 500 messages and custom keyword. The offer has no commitments. Upgrade or cancel at anytime.

We also want the landing page to focus on the benefits and marketing advantages (found in benefits tab), possible uses: mobile coupons, reminders/alerts, contests, daily specials, etc. (more examples can be found in how it works tab), and how it works.

The landing page can link to other parts of the site or use any information from other parts of the site. Our logo is attached in files. We want the design to match the overall color scheme of the site.

Target Market(s)

US based customers, business owners.

Industry/Entity Type

Marketing

Coding

Coded - Design and coding required

Number of Pages Required

1 page

Requirements
Must have
• See project description.
Nice to have
• See project description and any additional ideas welcomed from the designer.

```html
<!DOCTYPE html>
<html lang="en">
<head>
<meta charset="utf-8">
<title>MsgZeta – Cost-Effective SMS Messaging</title>
<link href="https://fonts.googleapis.com/css2?family=Lato:wght@300;400;700;900&family=Merriweather:wght@400;700&display=swap" rel="stylesheet">
<style>
:root{
  --red:#d0212b;
  --red-dark:#a8161f;
  --blue:#1ba1e2;
  --ink:#1f2329;
  --text:#555b63;
  --muted:#8a9099;
  --line:#e3e6ea;
  --dark:#1b2029;
  --footer:#2b3039;
  --footer-bar:#22262e;
  --white:#ffffff;
}
*{box-sizing:border-box;margin:0;padding:0}
html,body{width:1200px;height:3622px;overflow:hidden}
body{font-family:'Lato',sans-serif;color:var(--ink);background:var(--white);position:relative}
.section{position:absolute;left:0;width:1200px}
.abs{position:absolute}

/* header */
.site-header{top:0;height:121px;background:var(--white)}
.brand{left:130px;top:30px;display:flex;align-items:center;gap:10px}
.brand-mark{width:16px;height:16px;border-radius:50%;background:var(--red)}
.brand-name{font-family:'Lato',sans-serif;font-weight:900;font-size:34px;color:var(--red)}
.main-nav{right:120px;top:45px;display:flex;gap:8px}
.main-nav a{font-size:14px;color:var(--ink);text-decoration:none;padding:8px 18px;text-transform:uppercase;letter-spacing:.3px}
.main-nav a.active{background:var(--red);color:var(--white)}

/* hero */
.hero{top:121px;height:596px;background:linear-gradient(100deg,#d9dee3 0%,#c7cfd6 40%,#a7b2bc 70%,#8a939c 100%)}
.hero-photo{inset:0}
.hero-title{left:128px;top:190px;font-family:'Merriweather',serif;font-size:30px;line-height:38px;font-weight:700;color:var(--ink);letter-spacing:.5px}
.hero-text{left:128px;top:284px;width:380px;font-size:13px;line-height:20px;color:var(--ink)}
.btn-red{background:var(--red);color:var(--white);font-weight:700;text-transform:uppercase;display:flex;align-items:center;justify-content:center}
.hero-cta{left:128px;top:345px;width:162px;height:41px;font-size:17px}

/* why */
.why{top:717px;height:503px;background:var(--white)}
.why-title{left:130px;top:52px;font-family:'Merriweather',serif;font-size:28px;color:var(--ink)}
.why-rule{left:130px;top:113px;width:34px;height:3px;background:var(--red)}
.why-text{left:130px;top:138px;width:640px;font-size:12px;line-height:21px;color:var(--muted)}
.benefits{left:128px;top:270px;display:flex;align-items:center}
.benefit{display:flex;align-items:center;gap:16px;width:200px}
.benefit-icon{width:58px;height:58px;border-radius:50%;background:var(--blue);display:flex;align-items:center;justify-content:center}
.benefit-label{font-size:13px;line-height:18px;color:var(--text);text-transform:uppercase}
.benefit-slash{width:50px;height:60px;margin-right:10px}
.phone{border:2px solid #d5d9de;border-radius:34px;background:#f4f5f6}
.why-phone{left:840px;top:27px;width:198px;height:403px}
.phone-screen{position:absolute;left:12px;right:12px;top:56px;bottom:56px;background:linear-gradient(180deg,#1a7fd0,#2c9fe8)}
.phone-speaker{position:absolute;left:76px;top:26px;width:44px;height:5px;border-radius:3px;background:#cfd3d8}
.phone-button{position:absolute;left:82px;bottom:14px;width:32px;height:32px;border-radius:50%;border:2px solid #cfd3d8}

/* features */
.features{top:1220px;height:519px;background:linear-gradient(160deg,#2a2f39 0%,#171b22 55%,#1f242d 100%);overflow:hidden}
.features-title{top:60px;width:100%;text-align:center;font-size:27px;font-weight:900;color:var(--white);text-transform:uppercase}
.features-title span,.clients-title span{color:var(--blue)}
.feature{width:230px}
.feature h3{font-size:15px;font-weight:400;color:var(--blue);margin-bottom:6px}
.feature p{font-size:12px;line-height:19px;color:var(--white)}
.feature.right{text-align:right}
.feature-icon{width:55px;height:55px;border-radius:50%;background:var(--blue);display:flex;align-items:center;justify-content:center}
.feature-rings{left:300px;top:140px}
.feature-phone{left:507px;top:161px;width:193px;height:400px;border-color:#c9cdd2;background:#eef0f2}
.feature-phone .phone-screen{left:10px;right:10px;top:48px;bottom:0;background:linear-gradient(180deg,#2a8fde,#57b3ef 60%,#f2f4f6 60%)}

/* training */
.training{top:1739px;height:647px;background:var(--white)}
.training-title{top:70px;width:100%;text-align:center;font-size:27px;font-weight:900;text-transform:uppercase}
.training-quote{top:117px;width:100%;text-align:center;font-size:13px;color:var(--ink)}
.person{width:240px;text-align:center}
.person-ring{position:relative;width:193px;height:193px;margin:0 auto;border-radius:50%;background:#eef0f2;padding:10px}
.person-photo{width:100%;height:100%;border-radius:50%;background:linear-gradient(160deg,#c9d3dc,#8f9aa5)}
.social-dot{position:absolute;top:84px;width:26px;height:26px;border-radius:50%;background:#e3e6ea;border:2px solid var(--white)}
.social-dot.left{left:-8px}
.social-dot.right{right:-8px}
.person-name{margin-top:22px;font-size:21px;color:var(--ink)}
.person-role{margin-top:4px;font-size:14px;color:var(--text)}
.trial-cta{left:526px;top:501px;height:44px;display:flex}
.trial-price{width:44px;background:var(--red-dark);color:var(--white);font-weight:700;font-size:15px;display:flex;align-items:center;justify-content:center}
.trial-cta .btn-red{width:133px;font-size:15px;font-weight:400}
.trial-note{top:566px;width:100%;text-align:center;font-size:16px;color:var(--text)}

/* signup */
.signup{top:2386px;height:524px}
.signup-photo{inset:0;background:linear-gradient(110deg,#f1e3c4 0%,#b9a98d 25%,#5d604c 55%,#4d5a47 80%,#6b7466 100%)}
.signup-card{left:676px;top:72px;width:343px;height:379px;background:var(--white);padding:22px 18px;box-shadow:0 4px 18px rgba(0,0,0,.25)}
.signup-eyebrow{font-size:11px;font-weight:700;color:var(--blue);text-transform:uppercase}
.signup-heading{margin-top:14px;font-size:24px;line-height:30px;font-weight:700;color:var(--ink)}
.field-label{display:block;margin-top:20px;font-size:11px;font-weight:700;text-transform:uppercase}
.field-input{margin-top:8px;height:41px;border:1px solid #cfd3d8;background:#f7f8f9}
.signup-submit{margin-top:18px;width:164px;height:40px;font-size:14px;font-weight:400}

/* clients */
.clients{top:2910px;height:285px}
.clients-title{top:47px;width:100%;text-align:center;font-size:27px;font-weight:900;text-transform:uppercase}
.clients-sub{top:92px;width:100%;text-align:center;font-size:14px;color:var(--muted)}
.client-row{left:128px;top:159px;display:flex;gap:10px}
.client{width:150px;height:67px;border:1px solid var(--line);display:flex;align-items:center;justify-content:center;gap:8px;font-size:14px;font-weight:700;color:#3b6ea8}
.client-dot{width:14px;height:14px;border-radius:50%;background:#3b6ea8}

/* footer */
.site-footer{top:3195px;height:427px;background:var(--footer);color:#b9bec6}
.footer-col{top:72px}
.footer-col h4{font-size:15px;font-weight:900;color:var(--white);text-transform:uppercase;margin-bottom:26px}
.footer-col p{font-size:12px;line-height:18px}
.footer-links{list-style:none}
.footer-links li{font-size:12px;line-height:29px}
.footer-links li::before{content:"›";margin-right:8px;color:var(--white)}
.newsletter{display:flex;margin-top:26px}
.newsletter-input{width:204px;height:36px;background:#3c424c;color:#8d939c;font-size:11px;padding:11px 10px}
.newsletter-btn{width:36px;height:36px;background:var(--blue);display:flex;align-items:center;justify-content:center}
.contact-line{font-size:12px;line-height:18px}
.contact-phone{font-size:15px;font-weight:700;color:var(--white)}
.social-squares{display:flex;gap:6px;margin-top:16px}
.social-squares span{width:22px;height:22px;background:#484e58}
.footer-bar{left:0;bottom:0;width:100%;height:48px;background:var(--footer-bar);font-size:11px;display:flex;align-items:center;justify-content:space-between;padding:0 120px 0 147px}
</style>
</head>
<body>

<header class="section site-header">
  <div class="abs brand"><span class="brand-mark"></span><span class="brand-name">MsgZeta</span></div>
  <nav class="abs main-nav">
    <a class="active">Home</a><a>Our Pricing</a><a>Our Benefits</a><a>How It Works</a><a>Resellers</a><a>Sign Up</a>
  </nav>
</header>

<section class="section hero">
  <div class="abs hero-photo" role="img" aria-label="Photo of a smiling businessman on a park bench reading his phone, coffee cup beside him"></div>
  <h1 class="abs hero-title">THE MOST COST -EFFECTIVE<br>SMS MESSAGING</h1>
  <p class="abs hero-text">Lorem Ipsum is simply dummy text of the printing and typesetting industry. Lorem Ipsum has been the industry's standard</p>
  <a class="abs btn-red hero-cta">Try for 1 $</a>
</section>

<section class="section why">
  <h2 class="abs why-title">WHY MSGZETA</h2>
  <div class="abs why-rule"></div>
  <p class="abs why-text">Lorem Ipsum is simply dummy text of the printing and typesetting industry. Lorem Ipsum has been the industry's standard dummy text , ever since the 1500s, when an unknown printer took a galley .<br>otype and scrambled it to make a type specimen book. It has survived not only five centuries, but also the leap into electronic typesetting, remaining essentially unchanged.</p>
  <div class="abs benefits">
    <div class="benefit">
      <div class="benefit-icon"><svg width="28" height="28" viewBox="0 0 28 28" fill="none" stroke="#fff" stroke-width="2"><rect x="3" y="7" width="22" height="14" rx="2"/><circle cx="14" cy="14" r="3"/></svg></div>
      <div class="benefit-label">Save your<br>money</div>
    </div>
    <svg class="benefit-slash" viewBox="0 0 50 60"><line x1="40" y1="2" x2="10" y2="58" stroke="#c8ccd1" stroke-width="1.5"/></svg>
    <div class="benefit">
      <div class="benefit-icon"><svg width="28" height="28" viewBox="0 0 28 28" fill="none" stroke="#fff" stroke-width="2"><rect x="10" y="3" width="8" height="6"/><rect x="2" y="19" width="7" height="6"/><rect x="19" y="19" width="7" height="6"/><path d="M14 9v5M5 19v-5h18v5M14 14v5"/></svg></div>
      <div class="benefit-label">Do it<br>faster now</div>
    </div>
    <svg class="benefit-slash" viewBox="0 0 50 60"><line x1="40" y1="2" x2="10" y2="58" stroke="#c8ccd1" stroke-width="1.5"/></svg>
    <div class="benefit">
      <div class="benefit-icon"><svg width="28" height="28" viewBox="0 0 28 28" fill="none" stroke="#fff" stroke-width="2"><rect x="5" y="4" width="18" height="20" rx="2"/><path d="M10 14l3 3 6-6"/></svg></div>
      <div class="benefit-label">Remove<br>frustration</div>
    </div>
  </div>
  <div class="abs phone why-phone">
    <span class="phone-speaker"></span>
    <div class="phone-screen" role="img" aria-label="App login screen in blue"></div>
    <span class="phone-button"></span>
  </div>
</section>

<section class="section features">
  <h2 class="abs features-title">Feature at <span>a glance</span></h2>
  <svg class="abs feature-rings" width="600" height="420" viewBox="0 0 600 420" fill="none" stroke="#2e6f9c" stroke-width="1">
    <circle cx="303" cy="220" r="160" opacity=".5"/><circle cx="303" cy="220" r="200" opacity=".35"/><circle cx="303" cy="220" r="240" opacity=".2"/>
  </svg>
  <div class="abs phone feature-phone">
    <span class="phone-speaker" style="left:74px;top:20px"></span>
    <div class="phone-screen" role="img" aria-label="App profile screen for Nora Whitley with follow button and message list"></div>
  </div>

  <div class="abs feature" style="left:138px;top:158px"><h3>Send Bulk message</h3><p>Lorem Ipsum is simply dummy text of the printing and typesetting industry.</p></div>
  <div class="abs feature" style="left:138px;top:277px"><h3>Unlimited Subscribe</h3><p>Lorem Ipsum is simply dummy text of the printing and typesetting industry.</p></div>
  <div class="abs feature" style="left:138px;top:397px"><h3>Schedule Message</h3><p>Lorem Ipsum is simply dummy text of the printing and typesetting industry.</p></div>

  <div class="abs feature-icon" style="left:367px;top:137px"><svg width="24" height="24" viewBox="0 0 24 24" fill="none" stroke="#fff" stroke-width="2"><rect x="3" y="6" width="18" height="12"/><path d="M3 6l9 7 9-7"/></svg></div>
  <div class="abs feature-icon" style="left:367px;top:256px"><svg width="24" height="24" viewBox="0 0 24 24" fill="none" stroke="#fff" stroke-width="2"><rect x="4" y="4" width="16" height="16"/><path d="M8 12h8M12 8v8"/></svg></div>
  <div class="abs feature-icon" style="left:367px;top:376px"><svg width="24" height="24" viewBox="0 0 24 24" fill="none" stroke="#fff" stroke-width="2"><rect x="3" y="6" width="18" height="12"/><path d="M3 6l9 7 9-7"/></svg></div>

  <div class="abs feature-icon" style="left:773px;top:137px"><svg width="24" height="24" viewBox="0 0 24 24" fill="none" stroke="#fff" stroke-width="2"><path d="M4 5h16v11H9l-5 4z"/></svg></div>
  <div class="abs feature-icon" style="left:773px;top:256px"><svg width="24" height="24" viewBox="0 0 24 24" fill="none" stroke="#fff" stroke-width="2"><path d="M3 4h12v9H7l-4 3z"/><path d="M18 8h3v10l-3-2h-7v-3"/></svg></div>
  <div class="abs feature-icon" style="left:773px;top:376px"><svg width="24" height="24" viewBox="0 0 24 24" fill="none" stroke="#fff" stroke-width="2"><circle cx="12" cy="12" r="9"/><path d="M12 7v10M7 12h10"/></svg></div>

  <div class="abs feature right" style="left:849px;top:158px"><h3>Auto Responder</h3><p>Lorem Ipsum is simply dummy text of the printing and typesetting industry.</p></div>
  <div class="abs feature right" style="left:849px;top:277px"><h3>Live Chat Message</h3><p>Lorem Ipsum is simply dummy text of the printing and typesetting industry.</p></div>
  <div class="abs feature right" style="left:849px;top:397px"><h3>Ad Many More</h3><p>Lorem Ipsum is simply dummy text of the printing and typesetting industry.</p></div>
</section>

<section class="section training">
  <h2 class="abs training-title">Training Support</h2>
  <p class="abs training-quote">I switched suppliers &amp; now have msgzeta.net Training , Support &amp; Functionality are superb This will be a long term realtionship</p>

  <div class="abs person" style="left:153px;top:180px">
    <div class="person-ring"><div class="person-photo" role="img" aria-label="Portrait photo of Harlan D"></div><span class="social-dot left"></span><span class="social-dot right"></span></div>
    <div class="person-name">Harlan D,Owner</div><div class="person-role">Lorem Ipsum Dolar</div>
  </div>
  <div class="abs person" style="left:484px;top:180px">
    <div class="person-ring"><div class="person-photo" role="img" aria-label="Portrait photo of Curtis M"></div><span class="social-dot left"></span><span class="social-dot right"></span></div>
    <div class="person-name">Curtis M,VP</div><div class="person-role">Lorem Ipsum Dolar</div>
  </div>
  <div class="abs person" style="left:821px;top:180px">
    <div class="person-ring"><div class="person-photo" role="img" aria-label="Portrait photo of Talia R"></div><span class="social-dot left"></span><span class="social-dot right"></span></div>
    <div class="person-name">Talia R , CEO</div><div class="person-role">Lorem Ipsum Dolar</div>
  </div>

  <div class="abs trial-cta"><span class="trial-price">1$</span><a class="btn-red">Try it now</a></div>
  <p class="abs trial-note">Only $19.95 / month afterwards</p>
</section>

<section class="section signup">
  <div class="abs signup-photo" role="img" aria-label="Photo of a young woman with glasses sitting outdoors in warm sunlight, smiling at her phone"></div>
  <form class="abs signup-card">
    <div class="signup-eyebrow">Get started today</div>
    <h3 class="signup-heading">Get Started today, start your trial today</h3>
    <label class="field-label">First Name</label><div class="field-input"></div>
    <label class="field-label">Your Email</label><div class="field-input"></div>
    <div class="btn-red signup-submit">Start Now</div>
  </form>
</section>

<section class="section clients">
  <h2 class="abs clients-title">Our <span>Clients</span></h2>
  <p class="abs clients-sub">vs other sms messaging providers</p>
  <div class="abs client-row">
    <div class="client"><span class="client-dot"></span>Orvana</div>
    <div class="client">Kestrel Group</div>
    <div class="client"><span class="client-dot"></span>Halden</div>
    <div class="client">Pinecrest</div>
    <div class="client">Solvia</div>
    <div class="client"><span class="client-dot"></span>Brightmoor</div>
  </div>
</section>

<footer class="section site-footer">
  <div class="abs footer-col" style="left:147px;width:230px">
    <h4>Newsletter Subscribe</h4>
    <p>Lorem Ipsum is simply dummy text of the printing and typesetting industry. Lorem Ipsum has been.</p>
    <div class="newsletter"><div class="newsletter-input">Your email...</div><div class="newsletter-btn"><svg width="16" height="16" viewBox="0 0 16 16" fill="none" stroke="#fff" stroke-width="1.6"><rect x="1" y="3" width="14" height="10"/><path d="M1 3l7 6 7-6"/></svg></div></div>
  </div>
  <div class="abs footer-col" style="left:410px">
    <h4>Quick Links</h4>
    <ul class="footer-links"><li>Home</li><li>Wing Lane Premium</li><li>Meet the Mentors</li><li>Premium</li><li>Member Login</li></ul>
  </div>
  <div class="abs footer-col" style="left:676px">
    <h4>Industruy Solution</h4>
    <ul class="footer-links"><li>Wing Lane Premium Course</li><li>A Personal Wing Crew Mentors</li><li>A Community Of Wing Starters</li><li>Large Projects</li><li>Login</li><li>Pakaging Option</li></ul>
  </div>
  <div class="abs footer-col" style="left:934px">
    <h4>Contact Us</h4>
    <p class="contact-line">48 Larkspur Avenue<br>dolar sit amet Ad</p>
    <p class="contact-phone">+00 55 310 642 0198</p>
    <p class="contact-line">hello@ventrixmail.io</p>
    <div class="social-squares"><span></span><span></span><span></span></div>
  </div>
  <div class="abs footer-bar"><span>Copyright © 2015 MsgZeta . All Rights Reserved.</span><span>Terms &amp; Condition &nbsp;|&nbsp; Privacy Policy</span></div>
</footer>

</body>
</html>
```